Wine Label front and back

Need a front and back label. Front design is attached but want it fixed up and made eye catching Back label is going to be basic info attached as well. On the front label we will need Alc.By Vol. 14.8% and 2017 Sauvignon Blanc, Green Valley somewhere on the label.

Colors
fbf289
fbee3e
fdf9cf
cadf82
ec1f27

```html
<!DOCTYPE html>
<html lang="en">
<head>
<meta charset="utf-8">
<title>Marlowe Vineyards – Back Label</title>
<link href="https://fonts.googleapis.com/css2?family=PT+Sans:wght@400;700&display=swap" rel="stylesheet">
<style>
  :root {
    --label-yellow: #fbee3e;
    --pale-yellow: #fdf9cf;
    --soft-yellow: #fbf289;
    --leaf-green: #cadf82;
    --vine-green: #a9c95e;
    --wine-red: #ec1f27;
    --backdrop: #ece7df;
  }
  * { margin: 0; padding: 0; box-sizing: border-box; }
  html, body {
    width: 1200px;
    height: 834px;
    overflow: hidden;
    background: var(--backdrop);
  }
  .canvas {
    width: 1200px;
    height: 834px;
    display: flex;
    align-items: center;
    justify-content: center;
  }
  .back-label {
    width: 570px;
    height: 786px;
    background: var(--label-yellow);
    color: var(--wine-red);
    font-family: "PT Sans", sans-serif;
    text-align: center;
    padding: 118px 30px 28px;
    display: flex;
    flex-direction: column;
    align-items: center;
  }
  .site-url { font-size: 13px; margin-bottom: 22px; }
  .section { margin-bottom: 20px; font-size: 13px; line-height: 1.42; }
  .section-title { font-size: 13px; }
  .appointment { font-size: 13px; line-height: 1.42; margin-top: 8px; }
  .brand-mark {
    margin-top: 34px;
    display: flex;
    flex-direction: column;
    align-items: center;
    gap: 10px;
  }
  .vine-art {
    width: 160px;
    height: 96px;
    border-radius: 48px;
    background: radial-gradient(ellipse at center, var(--leaf-green) 0%, var(--vine-green) 55%, var(--label-yellow) 100%);
  }
  .brand-name {
    font-size: 20px;
    font-weight: 700;
    letter-spacing: 1px;
  }
</style>
</head>
<body>
<main class="canvas">
  <section class="back-label">
    <p class="site-url">www.HillcrestWine.com</p>

    <div class="section wine-club">
      <p class="section-title">WINE CLUB</p>
      <p>~ Wine Club Members have complimentary tastings ~</p>
      <p>Benefits</p>
      <p>Member Only Events</p>
      <p>20% Off All Hillcrest Wines</p>
      <p>40% Off Yearly Wine Club Anniversary (1 case max)</p>
      <p>20% Off Merchandise</p>
      <p>Complimentary Tasting</p>
    </div>

    <div class="section pick-up">
      <p class="section-title">Pick Up Options</p>
      <p>Each shipment is $119.00 and will include 3/4 bottles of our hand selected wine</p>
      <p>You can choose Quarterly, Monthly or Bi-Monthly Pick Ups</p>
    </div>

    <div class="section custom-club">
      <p class="section-title">Private Custom Club</p>
      <p>Our private corporate custom wine club creates a</p>
      <p>wine club that works with your members.</p>
      <p>You are the final tastemaker and we customize</p>
      <p>the items that most appeal to your group.</p>
      <p>*Items are limited, some restrictions apply,</p>
      <p>please contact us for additional details.</p>
    </div>

    <div class="appointment">
      <p>To set up an appointment to discuss your private custom club</p>
      <p>Call 707-555-0142 or Email info@HillcrestWine.com</p>
    </div>

    <div class="brand-mark">
      <div class="vine-art" role="img" aria-label="Grapevine illustration with green leaves"></div>
      <p class="brand-name">Marlowe Vineyards</p>
    </div>
  </section>
</main>
</body>
</html>
```